Zielgruppe
Wir sind ein Landwirtschaftsbetrieb für Obstbau und unsere Kunden sind hauptsächlich Privatpersonen und Familien aus der Region sowie Kleinbetriebe wie z. B. regionale Shops.
Aufgabenstellung
Wir benötigen Flaschenetiketten für Fruchtsäfte (3 verschiedene Sorten: Marillennektar, Pfirsichnektar, Kirschennektar) für 0,75 und 0,25 Liter Flaschen und für Schnaps und Liköre (Marillen, Kirschen, Pfirsich, Zwetschke, Kriecherl).
Wir würden eine Vorderseite, die das Design und die Pflichtangaben enthält, bevorzugen.
Die Schrift der Pflichtangaben muss wie folgt ausgeführt werden: Etiketten bis 80 cm2 Kleinbuchstaben mind. 0,9 mm, ab 80 cm2 Kleinbuchstaben mind. 1,2 mm, Großbuchstaben immer mind. 2 mm, das Feld benötigt in etwa 3,5 x 7 cm Platz. Für das Design gibt es noch keine fixe Größe.
Bitte keine Fotos von 'echtem' Obst verwenden.

```html
<!DOCTYPE html>
<html lang="de">
<head>
<meta charset="utf-8">
<title>Marillennektar – Etikett 0,75 l</title>
<link href="https://fonts.googleapis.com/css2?family=Oswald:wght@700&family=Poppins:ital,wght@0,400;0,600;0,700;1,800&display=swap" rel="stylesheet">
<style>
  :root {
    --page: #ffffff;
    --label-dark: #0d0d0d;
    --sheen: #9c9c9c;
    --apricot: #e8720c;
    --apricot-soft: #f0a23c;
    --claim: #e8531a;
    --white: #ffffff;
    --rule: #bdbdbd;
  }
  * { margin: 0; padding: 0; box-sizing: border-box; }
  html, body { width: 1200px; height: 1200px; overflow: hidden; background: var(--page); }
  body { position: relative; font-family: "Poppins", sans-serif; color: var(--white); }

  .label {
    position: absolute; left: 283px; top: 57px; width: 633px; height: 1085px;
    background: linear-gradient(90deg, #2a2a2a 0%, var(--sheen) 13%, #3a3a3a 26%, var(--label-dark) 55%, #1a1a1a 70%, #8a8a8a 88%, #2e2e2e 100%);
    overflow: hidden;
  }

  .brand {
    position: absolute; left: 40px; top: 205px; width: 420px;
    display: flex; align-items: center; justify-content: center; gap: 14px;
    font-weight: 600; font-size: 30px; letter-spacing: 1px; color: var(--white);
  }
  .brand-dot { width: 22px; height: 22px; border-radius: 50%; background: var(--claim); flex: none; }

  .producer { position: absolute; left: 0; width: 500px; text-align: center; font-weight: 600; font-size: 23px; line-height: 1; }
  .producer-name { top: 414px; }
  .producer-address { top: 451px; }

  .tree-art {
    position: absolute; left: 5px; top: 490px; width: 445px; height: 421px;
    background: radial-gradient(ellipse 60% 48% at 50% 42%, var(--apricot-soft) 0%, rgba(240,162,60,0.75) 55%, rgba(240,162,60,0) 100%);
  }

  .rule { position: absolute; left: 59px; width: 391px; height: 1px; background: var(--rule); }
  .rule-top { top: 594px; }
  .rule-bottom { top: 885px; }

  .ingredients {
    position: absolute; left: 20px; top: 635px; width: 462px;
    text-align: center; font-size: 20px; line-height: 32.5px; color: var(--white);
  }

  .claim {
    position: absolute; left: 0; top: 910px; width: 500px; text-align: center;
    font-weight: 800; font-style: italic; font-size: 25px; line-height: 35px; color: var(--claim);
  }

  .bottom-row { position: absolute; left: 40px; top: 1025px; width: 545px; height: 45px; }
  .best-before { position: absolute; left: 0; top: 4px; font-size: 26px; }
  .volume { position: absolute; left: 301px; top: -6px; font-weight: 600; font-size: 43px; line-height: 1; }
  .volume-e { font-weight: 400; }
  .box { position: absolute; left: 507px; top: 3px; width: 33px; height: 33px; background: var(--white); }

  .product-name { position: absolute; left: 477px; top: 71px; width: 109px; height: 921px; }
  .product-name text { font-family: "Oswald", sans-serif; font-weight: 700; fill: var(--apricot); }
</style>
</head>
<body>
  <main class="label">
    <div class="brand"><span class="brand-dot"></span>OBSTBAU-LINDNER</div>

    <p class="producer producer-name">Georg Lindner</p>
    <p class="producer producer-address">Lindenweg 12, A-2231 Feldau</p>

    <div class="tree-art" role="img" aria-label="Orange Illustration eines Marillenbaums mit dichter Krone"></div>

    <div class="rule rule-top"></div>
    <p class="ingredients">
      Zutaten: Wasser, Fruchtfleisch, Zucker,<br>
      Säuerungsmittel: Zitronensäure,<br>
      Antioxidationsmittel: Ascorbinsäure<br>
      Mindestens haltbar siehe Verschluss<br>
      Kühl und dunkel lagern, vor dem Öffnen<br>
      schütteln und innerhalb einiger Tage<br>
      konsumieren
    </p>
    <div class="rule rule-bottom"></div>

    <p class="claim">Marillen aus eigener<br>Produktion</p>

    <div class="bottom-row">
      <span class="best-before">Mindesthaltbar bis:</span>
      <span class="volume"><span class="volume-e">℮</span> 0,75 l</span>
      <span class="box"></span>
    </div>

    <svg class="product-name" viewBox="0 0 109 921" aria-label="Marillennektar">
      <text transform="translate(109 921) rotate(-90)" x="0" y="0" font-size="150" textLength="921" lengthAdjust="spacingAndGlyphs">MARILLENNEKTAR</text>
    </svg>
  </main>
</body>
</html>
```